India Export Business Card Design

We are a small company importing from India,
Antique furniture and textiles.
We would like a design with somthing of India in it.
IE: Camels, Tuk Tuks, People or maybe Taj Mahal.
Only one of the above suggestions, we do not want the card to be to busy.
We travel to India twice a year to get the product and then come home to New Zealand and sell it.
And must have our business name which is
Velmora Trading Company
Nz phone no. 64 9 317 6825
Mobile 64 21 573 162
Email bethany@velmoratrading.co.nz
Www.velmoratrading.co.nz

Also my name and position
Bethany Crowhurst
Director

Reason: I am awaiting for a design to come back with different colours. Many thanks

Target Market(s)

Indian heritage furniture and textiles in India also
New Zealand market for public to buy the goods that is bought in India

Industry/Entity Type

Travel

Contact Information for Business Card

Velmora Trading Company
17b Harlow Lane
RD 7 Papakura 2590
Auckland
New Zealand
email address which will be associated to our new website
website once we have it assigned

Requirements
Must have
• Company name and region.
Phone numbers
My name and title.
Nice to have
• I would like the card to portray India and as i said before, I like the idea of camels in a line with ropes between them like an animation.
But happy to see what other suggestions there are.

```html
<!DOCTYPE html>
<html lang="en">
<head>
<meta charset="utf-8">
<title>Velmora Trading Company – Business Card</title>
<link rel="stylesheet" href="https://fonts.googleapis.com/css2?family=Oswald:wght@500;600;700&display=swap">
<style>
  :root {
    --cyan: #00ffff;
    --cyan-soft: #9ffcfc;
    --ink: #4a4a4a;
    --grey: #8c8c8c;
    --paper: #ffffff;
  }
  html, body {
    margin: 0;
    padding: 0;
    overflow: hidden;
    background: var(--paper);
  }
  .card {
    position: relative;
    width: 1200px;
    height: 525px;
    background: var(--paper);
    overflow: hidden;
    font-family: "Oswald", "Arial Narrow", sans-serif;
  }
  .skyline {
    position: absolute;
    left: 600px;
    top: 8px;
    width: 460px;
    height: 206px;
    background: linear-gradient(to bottom, var(--cyan-soft), var(--cyan));
  }
  .band {
    position: absolute;
    left: 0;
    top: 241px;
    width: 1200px;
    height: 17px;
    background: var(--cyan);
  }
  .web-plate {
    position: absolute;
    left: 600px;
    top: 206px;
    width: 460px;
    height: 52px;
    background: var(--cyan);
  }
  .website {
    position: absolute;
    left: 628px;
    top: 205px;
    margin: 0;
    font-size: 31px;
    font-weight: 600;
    line-height: 52px;
    color: var(--paper);
    letter-spacing: 1.4px;
  }
  .brand-name {
    position: absolute;
    left: 106px;
    top: 110px;
    margin: 0;
    font-size: 112px;
    font-weight: 700;
    line-height: 1;
    color: var(--ink);
    letter-spacing: 0;
  }
  .brand-tagline {
    position: absolute;
    left: 108px;
    top: 258px;
    margin: 0;
    font-size: 44px;
    font-weight: 600;
    line-height: 1;
    color: var(--ink);
    letter-spacing: 0.6px;
  }
  .person {
    position: absolute;
    left: 110px;
    top: 336px;
    margin: 0;
  }
  .person-name {
    margin: 0;
    font-size: 30px;
    font-weight: 600;
    line-height: 36px;
    color: var(--ink);
    letter-spacing: 0.5px;
  }
  .person-title {
    margin: 0 0 12px;
    font-size: 22px;
    font-weight: 500;
    line-height: 28px;
    color: var(--grey);
    letter-spacing: 1px;
  }
  .address {
    margin: 0;
    font-style: normal;
    font-size: 20px;
    font-weight: 500;
    line-height: 27px;
    color: var(--grey);
    letter-spacing: 0.5px;
  }
  .contact-label {
    position: absolute;
    left: 938px;
    width: 262px;
    height: 35px;
    margin: 0;
    padding-left: 8px;
    box-sizing: border-box;
    background: var(--cyan);
    color: var(--paper);
    font-size: 29px;
    font-weight: 600;
    line-height: 35px;
    letter-spacing: 0.5px;
  }
  .contact-value {
    position: absolute;
    margin: 0;
    color: var(--grey);
    font-size: 30px;
    font-weight: 600;
    line-height: 1;
    letter-spacing: 1px;
  }
  .label-phone { top: 285px; }
  .value-phone { left: 928px; top: 326px; }
  .label-mobile { top: 365px; }
  .value-mobile { left: 955px; top: 405px; }
  .label-email { top: 451px; }
  .value-email { left: 656px; top: 490px; letter-spacing: 1.4px; }
</style>
</head>
<body>
  <main class="card">
    <div class="skyline" role="img" aria-label="Cyan silhouette of an Indian city skyline with domes and minarets"></div>
    <div class="band"></div>
    <div class="web-plate"></div>
    <p class="website">WWW.VELMORATRADING.CO.NZ</p>

    <h1 class="brand-name">VELMORA</h1>
    <p class="brand-tagline">TRADING COMPANY</p>

    <section class="person">
      <p class="person-name">BETHANY CROWHURST</p>
      <p class="person-title">DIRECTOR</p>
      <address class="address">17B HARLOW LANE<br>RD 7 PAPAKURA 2590<br>AUCKLAND, NEW ZEALAND</address>
    </section>

    <p class="contact-label label-phone">NZ PHONE NO</p>
    <p class="contact-value value-phone">64 9 3176825</p>

    <p class="contact-label label-mobile">MOBILE</p>
    <p class="contact-value value-mobile">021573162</p>

    <p class="contact-label label-email">EMAIL</p>
    <p class="contact-value value-email">BETHANY@VELMORATRADING.CO.NZ</p>
  </main>
</body>
</html>
```